Verpackungen für kleine Imkerei
Zielgruppe
Wir sind eine kleine Imkerei aus dem Aargau (Schweiz) und stellen zusammen mit unseren glücklichen Bienen feinsten Honig her. Gerne möchten wir unseren visuelle Kommunikation nach aussen mit Hilfe eines neuen Etiketts verbessern.
Aufgabenstellung
Das Etikett muss rechteckig sein und wir auf einem runden Glas aufgeklebt. Die Maximalgrösse ist 210x45mm (beim 500g Glas) und entsprechend kleiner bei kleineren Einheiten. Wir möchten ein Grunddesign, welches adaptierbar ist auf die weiteren Sorten. (Waldhonig, Blütenhonig, cremiger Blütenhonig, Zürcher Stadthonig, Badener Stadthonig, Lenzburger Stadthonig). Barcode muss keinen eingefügt werden, nur die gesetzlichen Daten müssen auf dem Etiektt stehen. Weitere Wünsche und Anmerkungen befinden sich im pdf.
Sollten Dateien oder Bilder nachgereicht werden, bitte melden!

```html
<!DOCTYPE html>
<html lang="de">
<head>
<meta charset="utf-8">
<title>Summgut – Etikett Blütenhonig</title>
<link href="https://fonts.googleapis.com/css2?family=Amatic+SC:wght@700&display=swap" rel="stylesheet">
<style>
  :root {
    --page-bg: #eeeeee;
    --label-white: #ffffff;
    --band-pink: #f2a7bd;
    --comb-pink: #f9d6e1;
    --text-white: #ffffff;
    --text-dark: #1c1c1c;
    --accent-pink: #e0577f;
  }
  html, body {
    margin: 0;
    padding: 0;
    width: 1200px;
    height: 800px;
    overflow: hidden;
    background: var(--page-bg);
  }
  .canvas {
    position: relative;
    width: 1200px;
    height: 800px;
    display: flex;
    align-items: center;
    justify-content: center;
    font-family: "Amatic SC", cursive;
  }
  .label {
    position: relative;
    width: 1100px;
    height: 234px;
    background: var(--label-white);
    box-shadow: 0 3px 10px rgba(0,0,0,0.12);
    overflow: hidden;
  }
  .label__top {
    position: absolute;
    inset: 0 0 auto 0;
    height: 134px;
  }
  .comb-area {
    position: absolute;
    top: 0;
    height: 134px;
    width: 300px;
  }
  .comb-area--left {
    left: 0;
    background: linear-gradient(90deg, var(--comb-pink) 0%, rgba(249,214,225,0.25) 100%);
    opacity: 0.55;
  }
  .comb-area--right {
    right: 0;
    background: linear-gradient(270deg, var(--comb-pink) 0%, rgba(249,214,225,0.25) 100%);
    opacity: 0.55;
  }
  .brand {
    position: absolute;
    left: 50%;
    top: 30px;
    transform: translateX(-50%);
    display: flex;
    align-items: center;
    gap: 14px;
    color: var(--text-dark);
    font-size: 64px;
    line-height: 1;
  }
  .brand__dot {
    width: 14px;
    height: 14px;
    border-radius: 50%;
    background: var(--text-dark);
  }
  .label__band {
    position: absolute;
    left: 0;
    right: 0;
    bottom: 0;
    height: 100px;
    background: var(--band-pink);
    color: var(--text-white);
  }
  .legal {
    position: absolute;
    left: 24px;
    top: 10px;
    font-size: 16px;
    line-height: 17px;
  }
  .legal__title, .legal strong {
    font-size: 18px;
  }
  .variety {
    position: absolute;
    left: 50%;
    top: 10px;
    transform: translateX(-50%);
    text-align: center;
  }
  .variety__name {
    font-size: 34px;
    line-height: 38px;
    letter-spacing: 1px;
  }
  .variety__name::before, .variety__name::after {
    content: "•";
    margin: 0 6px;
  }
  .variety__icon {
    display: block;
    margin: 4px auto 2px;
  }
  .variety__weight {
    font-size: 17px;
    color: var(--accent-pink);
  }
  .producer {
    position: absolute;
    left: 920px;
    top: 10px;
    font-size: 16px;
    line-height: 17px;
  }
  .producer__name {
    font-size: 18px;
  }
  .producer__web {
    margin-top: 17px;
  }
</style>
</head>
<body>
<main class="canvas">
  <section class="label">
    <div class="label__top">
      <div class="comb-area comb-area--left" role="img" aria-label="Dekoratives Wabenmuster in zartem Rosa"></div>
      <div class="comb-area comb-area--right" role="img" aria-label="Dekoratives Wabenmuster in zartem Rosa"></div>
      <div class="brand"><span class="brand__dot"></span>Summgut</div>
    </div>
    <div class="label__band">
      <div class="legal">
        <div class="legal__title">Schweizer Blütenhonig</div>
        <div>Honig gut verschlossen, kühl (bei max. 15°)</div>
        <div>Dunkel &amp; trocken lagern</div>
        <div><strong>Mindestens haltbar</strong> bis August 2022</div>
        <div>Warenlos Nr. 01092018</div>
      </div>
      <div class="variety">
        <div class="variety__name">Blütenhonig</div>
        <svg class="variety__icon" width="24" height="24" viewBox="0 0 24 24" aria-hidden="true">
          <circle cx="12" cy="12" r="9" fill="none" stroke="#ffffff" stroke-width="1.6"/>
          <circle cx="12" cy="12" r="3" fill="none" stroke="#ffffff" stroke-width="1.6"/>
        </svg>
        <div class="variety__weight">500g Nettogewicht</div>
      </div>
      <div class="producer">
        <div class="producer__name">Ursula &amp; Beat Karrigo</div>
        <div>Lindenmattweg 4</div>
        <div>5612 Mühlewil</div>
        <div class="producer__web">www.summgut.ch</div>
      </div>
    </div>
  </section>
</main>
</body>
</html>
```